PowerPoint Design Project

Powerpoint design for an online marketing agency.
PP will be used as a WhitePaper to showcase our expertise.
Our USP is that we use data for marketing so the design must reflect this with charts and graphs.
A set of images is available in our flickr account
http://www.pixelvault.example/photos/kelmora/sets/48302916574021983/with/3104827561/
We already have written real content for the PP for you to work with.
Updates

1. I have added a sample of the content a 2-page extract in a word document. The full document is around 15 pages.
2. While the finished piece is to be in PowerPoint format, it will also be used as a White Paper so the design should reflect this - i.e it should be able to be read like it was a well designed Word document not just a PP
3. The design you see in the sample 2-page document is just for illustration purposes it is not intended to influence the final design at all. So for example it currently has some pull-quotes in black boxes - that is just to show what they are and I don't want the final piece to have black boxes around quotes.
4. I've been asked to make this project guaranteed: as this is the first time I've used ArtHivePro I'm going to keep it as a standard project but we are committed to the work.
5. The current deadline is for the START of design work. We need the completed design by 21 September, so there is plenty of time to schedule this in with your other work.
Many thanks
Nigel 

The designs shown so far would not be suitable for turning into a WhitePaper. For example the bars across the top of the design create a break at the start of each page rather than emphasise the continuous nature of the document. 

Here is an example of some great design for a similar project - and we've uploaded another sample as a file

http://www.surgeloft.example/downloads/[SURGE]-what-its-like-working-

If you asked me for some ideas on the feel of the design I would say:

1. Bold - it has to look interesting - corporate world but it doesn't need to feel dull/grey
2. Exciting 
3. Precise - easy to read , not a fussy design

Target Market(s)

Business developers, sales managers, CEOs of companies with over 5 employees but without their own marketing department

Industry/Entity Type

Marketing

Requirements
Must have
• Flawless design that says "this company is smart and means business"
Nice to have
• the powerpoint should lend itself to easy file/saveas to be delivered as a PDF and for individual slides to be extracted for presentation, or use as images in blog posts etc (so for example any page number must be easy to remove).
Should not have
• no cartoons, no line drawings, nothing to obscure easy legibility

```html
<!DOCTYPE html>
<html lang="en">
<head>
<meta charset="utf-8">
<title>World Internet Penetration Rates by Geographic Regions 2011</title>
<link href="https://fonts.googleapis.com/css2?family=Roboto+Condensed:wght@400;700&family=Arimo:wght@400;700&display=swap" rel="stylesheet">
<style>
  :root {
    --navy: #0d2f6b;
    --navy-deep: #082457;
    --brand: #1b3f86;
    --ink: #1a1a1a;
    --bar-red: #c8262b;
    --bar-red-light: #e0494a;
    --bar-red-dark: #9e1518;
    --bar-gold: #e8b400;
    --bar-gold-light: #f7d23a;
    --plot-bg: #f3dede;
    --grid: #c9a3a3;
    --value: #5a0d10;
    --footer-blue: #c9dcec;
    --muted: #8a8a8a;
  }
  * { margin: 0; padding: 0; box-sizing: border-box; }
  html, body { width: 1200px; height: 900px; overflow: hidden; background: #fff; }
  .slide { position: relative; width: 1200px; height: 900px; overflow: hidden; background: #fff; }

  .slide-header {
    position: absolute; left: 0; top: 0; width: 1200px; height: 120px;
    background: #fff;
  }
  .header-rule {
    position: absolute; left: 57px; bottom: 10px; width: 1119px; height: 2px;
    background: linear-gradient(90deg, var(--navy) 0%, rgba(13,47,107,0.35) 60%, rgba(13,47,107,0) 100%);
  }
  .slide-title {
    position: absolute; left: 57px; top: 18px;
    font-family: "Roboto Condensed", sans-serif; font-weight: 700;
    font-size: 33px; line-height: 42px; color: var(--navy-deep);
  }
  .brand-name {
    position: absolute; right: 24px; top: 8px;
    font-family: "Roboto Condensed", sans-serif; font-weight: 700;
    font-size: 84px; line-height: 100px; color: var(--brand); letter-spacing: -1px;
  }

  .chart-card {
    position: absolute; left: 37px; top: 147px; width: 983px; height: 633px;
    background: #fff; border-radius: 6px;
    box-shadow: 0 2px 10px rgba(0,0,0,0.22);
  }
  .chart-card svg { display: block; }
  .category { font-family: "Arimo", sans-serif; font-weight: 700; font-size: 19px; fill: var(--ink); }
  .value { font-family: "Arimo", sans-serif; font-weight: 700; font-size: 18px; fill: var(--value); }
  .tick { font-family: "Arimo", sans-serif; font-weight: 700; font-size: 18px; fill: var(--ink); }
  .axis-title { font-family: "Arimo", sans-serif; font-weight: 700; font-size: 19px; fill: var(--ink); }

  .slide-footer {
    position: absolute; left: 0; top: 795px; width: 1200px; height: 105px;
    background: linear-gradient(180deg, #ffffff 0%, var(--footer-blue) 45%, #eaf2f9 100%);
  }
  .footer-curve { position: absolute; left: 0; top: 0; }
  .copyright {
    position: absolute; left: 45px; top: 844px;
    font-family: "Roboto Condensed", sans-serif; font-size: 18px; color: var(--muted);
  }
  .page-number {
    position: absolute; left: 1084px; top: 784px; width: 66px; height: 66px;
    border-radius: 50%; background: #fff; border: 3px solid var(--brand);
    font-family: "Roboto Condensed", sans-serif; font-weight: 700; font-size: 24px;
    color: var(--navy-deep); display: flex; align-items: center; justify-content: center;
  }
</style>
</head>
<body>
<div class="slide">
  <header class="slide-header">
    <h1 class="slide-title">World Internet Penetration Rates by<br>Geographics Regions -2011</h1>
    <div class="brand-name">kelmora</div>
    <div class="header-rule"></div>
  </header>

  <section class="chart-card">
    <svg width="983" height="633" viewBox="0 0 983 633" role="img" aria-label="Bar chart of internet penetration rates by region, 2011">
      <defs>
        <linearGradient id="barRed" x1="0" y1="0" x2="0" y2="1">
          <stop offset="0" stop-color="var(--bar-red-light)"/>
          <stop offset="0.5" stop-color="var(--bar-red)"/>
          <stop offset="1" stop-color="var(--bar-red-dark)"/>
        </linearGradient>
        <linearGradient id="barGold" x1="0" y1="0" x2="0" y2="1">
          <stop offset="0" stop-color="var(--bar-gold-light)"/>
          <stop offset="1" stop-color="var(--bar-gold)"/>
        </linearGradient>
      </defs>

      <rect class="plot-area" x="183.5" y="25" width="757.5" height="515" fill="var(--plot-bg)"/>
      <g class="gridlines" stroke="var(--grid)" stroke-width="1">
        <line x1="267.7" y1="25" x2="267.7" y2="540"/>
        <line x1="351.8" y1="25" x2="351.8" y2="540"/>
        <line x1="436" y1="25" x2="436" y2="540"/>
        <line x1="520.2" y1="25" x2="520.2" y2="540"/>
        <line x1="604.4" y1="25" x2="604.4" y2="540"/>
        <line x1="688.5" y1="25" x2="688.5" y2="540"/>
        <line x1="772.7" y1="25" x2="772.7" y2="540"/>
        <line x1="856.9" y1="25" x2="856.9" y2="540"/>
        <line x1="941" y1="25" x2="941" y2="540"/>
      </g>
      <g class="axes" stroke="#666" stroke-width="1.5">
        <line x1="183.5" y1="25" x2="183.5" y2="540"/>
        <line x1="183.5" y1="540" x2="941" y2="540"/>
        <line x1="176" y1="82.5" x2="183.5" y2="82.5"/>
        <line x1="176" y1="148.5" x2="183.5" y2="148.5"/>
        <line x1="176" y1="214.5" x2="183.5" y2="214.5"/>
        <line x1="176" y1="280.5" x2="183.5" y2="280.5"/>
        <line x1="176" y1="346.5" x2="183.5" y2="346.5"/>
        <line x1="176" y1="412.5" x2="183.5" y2="412.5"/>
        <line x1="176" y1="478.5" x2="183.5" y2="478.5"/>
      </g>

      <g class="bars">
        <rect x="183.5" y="36" width="661.6" height="27" fill="url(#barRed)"/>
        <rect x="183.5" y="102" width="568.1" height="27" fill="url(#barRed)"/>
        <rect x="183.5" y="168" width="516" height="27" fill="url(#barRed)"/>
        <rect x="183.5" y="234" width="332.5" height="27" fill="url(#barRed)"/>
        <rect x="183.5" y="300" width="299.6" height="27" fill="url(#barRed)"/>
        <rect x="183.5" y="366" width="275.2" height="27" fill="url(#barGold)"/>
        <rect x="183.5" y="432" width="220.5" height="27" fill="url(#barRed)"/>
        <rect x="183.5" y="498" width="113.6" height="27" fill="url(#barRed)"/>
      </g>

      <g class="values">
        <text class="value" x="857" y="56">78.6%</text>
        <text class="value" x="764" y="122">67.5%</text>
        <text class="value" x="712" y="188">61.3%</text>
        <text class="value" x="528" y="254">39.5%</text>
        <text class="value" x="495" y="320">35.6%</text>
        <text class="value" x="471" y="386">32.7%</text>
        <text class="value" x="416" y="452">26.2%</text>
        <text class="value" x="309" y="518">13.5%</text>
      </g>

      <g class="categories" text-anchor="end">
        <text class="category" x="163" y="56">North America</text>
        <text class="category" x="163" y="112">Oceania /</text>
        <text class="category" x="163" y="134">Australia</text>
        <text class="category" x="163" y="188">Europe</text>
        <text class="category" x="163" y="244">Latin America /</text>
        <text class="category" x="150" y="266">Caribbean</text>
        <text class="category" x="163" y="320">Middle East</text>
        <text class="category" x="163" y="386">World, Avg.</text>
        <text class="category" x="163" y="452">Asia</text>
        <text class="category" x="163" y="518">Africa</text>
      </g>

      <g class="ticks" text-anchor="middle">
        <text class="tick" x="183.5" y="580">0</text>
        <text class="tick" x="267.7" y="580">10%</text>
        <text class="tick" x="351.8" y="580">20%</text>
        <text class="tick" x="436" y="580">30%</text>
        <text class="tick" x="520.2" y="580">40%</text>
        <text class="tick" x="604.4" y="580">50%</text>
        <text class="tick" x="688.5" y="580">60%</text>
        <text class="tick" x="772.7" y="580">70%</text>
        <text class="tick" x="856.9" y="580">80%</text>
        <text class="tick" x="941" y="580">90%</text>
      </g>
      <text class="axis-title" x="562" y="620" text-anchor="middle">Penetration Rate</text>
    </svg>
  </section>

  <footer class="slide-footer">
    <svg class="footer-curve" width="1200" height="105" viewBox="0 0 1200 105" aria-hidden="true">
      <path d="M0 30 C 400 -5, 800 -5, 1200 25 L1200 0 L0 0 Z" fill="#ffffff" opacity="0.85"/>
      <path d="M0 36 C 400 2, 800 2, 1200 31" fill="none" stroke="#ffffff" stroke-width="3"/>
    </svg>
  </footer>
  <div class="copyright">Copyright@kelmora</div>
  <div class="page-number">01</div>
</div>
</body>
</html>
```